Business Stationery Design

I would like to get some stationery designed for my company. The stationery should include a letterhead, envelope, and business card. We are a technology consulting company specializing in Healthcare IT, and Education management systems. The colors of the stationery should match the logo. The logo is uploaded.

Target Market(s)

Hospitals, Clinics. Doctors offices. Private Schools.

Industry/Entity Type

Business

```html
<!DOCTYPE html>
<html lang="en">
<head>
<meta charset="utf-8">
<title>Clearbrook Advisory Group – Letterhead</title>
<link href="https://fonts.googleapis.com/css2?family=Cabin:wght@400&display=swap" rel="stylesheet">
<style>
  :root {
    --backdrop: #cfe6b6;
    --paper: #ffffff;
    --brand-green: #6cb52d;
    --deep-green: #4f9a1b;
    --light-green: #8fd044;
    --accent-gold: #f0b323;
    --text-grey: #6f6f6f;
  }
  * { margin: 0; padding: 0; box-sizing: border-box; }
  html, body {
    width: 1200px;
    height: 784px;
    overflow: hidden;
    background: var(--backdrop);
    font-family: "Cabin", sans-serif;
  }
  .stage {
    width: 1200px;
    height: 784px;
    display: flex;
    align-items: center;
    justify-content: center;
  }
  .letterhead {
    position: relative;
    width: 510px;
    height: 720px;
    background: var(--paper);
    box-shadow: 0 6px 18px rgba(60, 100, 30, 0.18);
    overflow: hidden;
  }
  .brand {
    position: absolute;
    top: 30px;
    left: 34px;
    display: flex;
    align-items: center;
    gap: 7px;
  }
  .brand-dot {
    width: 12px;
    height: 12px;
    border-radius: 50%;
    background: var(--brand-green);
  }
  .brand-name {
    font-size: 19px;
    font-weight: 400;
    color: var(--brand-green);
    letter-spacing: 0.2px;
  }
  .contact {
    position: absolute;
    top: 30px;
    right: 30px;
    text-align: right;
  }
  .contact-company {
    font-size: 14px;
    color: var(--brand-green);
    margin-bottom: 5px;
  }
  .contact-line {
    font-size: 7.5px;
    color: var(--text-grey);
    line-height: 12px;
  }
  .contact-line .bullet {
    display: inline-block;
    width: 5px;
    height: 5px;
    background: var(--brand-green);
    margin: 0 3px 0 5px;
    vertical-align: middle;
  }
  .footer-wave {
    position: absolute;
    left: 0;
    bottom: 0;
    width: 510px;
    height: 200px;
  }
</style>
</head>
<body>
<main class="stage">
  <article class="letterhead">
    <header class="brand">
      <span class="brand-dot"></span>
      <span class="brand-name">Clearbrook</span>
    </header>

    <address class="contact">
      <p class="contact-company">Clearbrook Advisory Group</p>
      <p class="contact-line"><span class="bullet"></span>2150 Example Ave, Suite 300, Austin, TX 78701</p>
      <p class="contact-line"><span class="bullet"></span>(555) 014-2271<span class="bullet"></span>(555) 014-8724</p>
      <p class="contact-line"><span class="bullet"></span>info@clearbrookadvisory.com<span class="bullet"></span>www.clearbrookadvisory.com</p>
    </address>

    <svg class="footer-wave" viewBox="0 0 510 200" aria-hidden="true">
      <defs>
        <linearGradient id="waveGreen" x1="0" y1="0" x2="1" y2="1">
          <stop offset="0" stop-color="var(--light-green)"/>
          <stop offset="0.5" stop-color="var(--deep-green)"/>
          <stop offset="1" stop-color="var(--light-green)"/>
        </linearGradient>
      </defs>
      <path d="M0,48 C40,70 90,110 180,150 C290,195 420,200 500,200 L0,200 Z" fill="url(#waveGreen)"/>
      <path d="M0,36 C45,60 95,100 185,140 C295,185 420,194 505,196" fill="none" stroke="var(--accent-gold)" stroke-width="6"/>
      <path d="M0,22 C50,48 100,88 190,128" fill="none" stroke="var(--brand-green)" stroke-width="3.5"/>
    </svg>
  </article>
</main>
</body>
</html>
```